RKW Automotive needs a catchy banner design

We need a design for a banner to be displayed on the fence in the outfield of a baseball stadium to show off our company and have people interested in what we do. We need something catchy that's going to attract people to look over at our banner.
We are a
Complete Automotive Service Company
Tires - Service - Repair - Diesel
We are in a Town called Braxton-Hills
(555)314-2096 we would like the phone number to be a descent size so when you are in the stands you can read it.
I have attached what we came up with but like I said we need it to pop more and make the viewer that's looking at it want to look us up.
The Banner size is 24ft long and 10ft tall

```html
<!DOCTYPE html>
<html lang="en">
<head>
<meta charset="utf-8">
<title>RKW Automotive – Outfield Banner</title>
<link rel="stylesheet" href="https://fonts.googleapis.com/css2?family=Montserrat:wght@700;800&family=Orbitron:wght@900&family=Saira+Semi+Condensed:wght@700&display=swap">
<style>
  :root {
    --black: #000000;
    --white: #ffffff;
    --accent-blue: #2a8cf0;
    --panel-navy: #0a1560;
    --panel-royal: #1530a8;
    --engine-light: #2a5cb0;
    --engine-dark: #040c24;
  }
  html, body {
    margin: 0;
    padding: 0;
    width: 1200px;
    height: 500px;
    overflow: hidden;
    background: var(--black);
  }
  .banner {
    display: block;
    width: 1200px;
    height: 500px;
  }
  .headline {
    font-family: "Saira Semi Condensed", sans-serif;
    font-weight: 700;
    font-size: 60px;
    fill: var(--white);
  }
  .service-list {
    font-family: "Orbitron", sans-serif;
    font-weight: 900;
    font-size: 74px;
    fill: var(--white);
  }
  .brand-name {
    font-family: "Montserrat", sans-serif;
    font-weight: 800;
    font-size: 30px;
    fill: var(--white);
  }
  .call-label {
    font-family: "Montserrat", sans-serif;
    font-weight: 700;
    font-size: 43px;
    fill: var(--white);
  }
  .call-number {
    font-family: "Montserrat", sans-serif;
    font-weight: 800;
    font-size: 56px;
    fill: var(--white);
  }
  .town {
    font-family: "Montserrat", sans-serif;
    font-weight: 800;
    font-size: 43px;
    fill: var(--accent-blue);
  }
</style>
</head>
<body>
<svg class="banner" viewBox="0 0 1200 500" xmlns="http://www.w3.org/2000/svg">
  <defs>
    <linearGradient id="engine-tone" x1="0" y1="0" x2="1" y2="1">
      <stop offset="0" stop-color="var(--engine-light)"/>
      <stop offset="0.55" stop-color="#163a80"/>
      <stop offset="1" stop-color="var(--engine-dark)"/>
    </linearGradient>
    <linearGradient id="panel-tone" x1="0" y1="1" x2="1" y2="0">
      <stop offset="0" stop-color="var(--panel-navy)"/>
      <stop offset="0.6" stop-color="#0d1d80"/>
      <stop offset="1" stop-color="var(--panel-royal)"/>
    </linearGradient>
  </defs>

  <rect class="top-band" x="0" y="0" width="1200" height="93" fill="var(--black)"/>
  <text class="headline" x="38" y="68" textLength="1124" lengthAdjust="spacing">COMPLETE AUTOMOTIVE SERVICE COMPANY</text>

  <rect class="hero-photo" x="0" y="93" width="920" height="321" fill="url(#engine-tone)"
        role="img" aria-label="Close-up photo of a car engine with pulleys and alternator, tinted blue"/>
  <polygon class="brand-panel" points="913,93 1200,93 1200,414 680,414" fill="url(#panel-tone)"/>

  <text class="service-list" x="42" y="219" textLength="701" lengthAdjust="spacingAndGlyphs">•TIRES•SERVICE</text>
  <text class="service-list" x="42" y="296" textLength="701" lengthAdjust="spacingAndGlyphs">•REPAIR•DEISEL</text>

  <text class="brand-name" x="1007" y="245" text-anchor="middle">RKW AUTOMOTIVE</text>

  <rect class="bottom-band" x="0" y="414" width="1200" height="86" fill="var(--black)"/>
  <text class="call-label" x="56" y="476" textLength="272" lengthAdjust="spacing">CALL NOW</text>
  <text class="call-number" x="350" y="478" textLength="389" lengthAdjust="spacingAndGlyphs">(555)314-2096</text>
  <text class="town" x="797" y="476" textLength="361" lengthAdjust="spacingAndGlyphs">BRAXTON-HILLS</text>
</svg>
</body>
</html>
```